A label for my commercially sold local honey. This is a LABEL not a logo

3 inches high
2 inches wide

Target Market(s)

Customers who like "local" honey

Logo Text

Wildflower Honey -- 100% Pure & Unfiltered -- Florida

Logo styles of interest
Wordmark Logo
Requirements
Must have
• Wildflower Honey -- 100% Pure & Unfiltered -- Florida

Florida should be dominant

3 inches high / 2 inches wide

```html
<!DOCTYPE html>
<html lang="en">
<head>
<meta charset="utf-8">
<title>Wildflower Honey Label</title>
<link href="https://fonts.googleapis.com/css2?family=Staatliches&family=Alfa+Slab+One&family=Schoolbell&display=swap" rel="stylesheet">
<style>
  :root {
    --ink: #0d0f10;
    --paper: #ffffff;
    --page: #ffffff;
    --shadow: rgba(0, 0, 0, 0.22);
  }
  * { margin: 0; padding: 0; box-sizing: border-box; }
  html, body {
    width: 1200px;
    height: 1200px;
    overflow: hidden;
    background: var(--page);
  }
  .canvas {
    position: relative;
    width: 1200px;
    height: 1200px;
  }
  .label {
    position: absolute;
    left: 267px;
    top: 100px;
    width: 667px;
    height: 1000px;
    background: var(--paper);
    box-shadow: 14px 18px 34px var(--shadow);
    color: var(--ink);
  }
  .label-frame {
    position: absolute;
    left: 30px;
    top: 30px;
    right: 31px;
    bottom: 31px;
    border: 11px solid var(--ink);
  }
  .product-title {
    position: absolute;
    left: 0;
    right: 0;
    top: 86px;
    text-align: center;
    font-family: "Staatliches", sans-serif;
    font-size: 58px;
    line-height: 54px;
    letter-spacing: 4px;
  }
  .brand-name {
    position: absolute;
    left: 0;
    right: 0;
    top: 380px;
    text-align: center;
    font-family: "Staatliches", sans-serif;
    font-size: 84px;
    line-height: 84px;
    letter-spacing: 6px;
  }
  .tagline-band {
    position: absolute;
    left: 41px;
    right: 42px;
    top: 754px;
    height: 65px;
    border-top: 3px solid var(--ink);
    border-bottom: 3px solid var(--ink);
    display: flex;
    align-items: center;
    justify-content: center;
  }
  .tagline {
    font-family: "Schoolbell", cursive;
    font-size: 34px;
    letter-spacing: 1px;
  }
  .origin {
    position: absolute;
    left: 0;
    right: 0;
    top: 856px;
    text-align: center;
    font-family: "Alfa Slab One", serif;
    font-size: 64px;
    line-height: 80px;
    letter-spacing: 5px;
  }
</style>
</head>
<body>
  <main class="canvas">
    <section class="label">
      <div class="label-frame"></div>
      <h1 class="product-title">Wildflower<br>Honey</h1>
      <p class="brand-name">Sunvale<br>Apiary</p>
      <div class="tagline-band">
        <p class="tagline">100% Pure &amp; Unfiltered</p>
      </div>
      <p class="origin">FLORIDA</p>
    </section>
  </main>
</body>
</html>
```